KVO-Business Card Design

I need a modern, professional business card design that includes my logo as the main feature, maybe the entire background with the contact info overlaying or even contact info on the back and the logo full frontal

Neat and organized placement of contact information

Would like to see options in black and white

Target Market(s)

real estate Developers, Construction managers, business and home owners

Industry/Entity Type

Construction

Contact Information for Business Card

KVO Construction
Danny Ferrante
General Contractor

Office: 1-888-902-7315 Ext #1
Cell: 215-730-4162
Fax: 1-888-902-7315

Font styles to use
Serif

Requirements
Must have
• title
• office #
• cell #
• Email
• website
Nice to have
• fax

```html
<!DOCTYPE html>
<html lang="en">
<head>
<meta charset="utf-8">
<title>KVO Construction – Business Card</title>
<link rel="stylesheet" href="https://fonts.googleapis.com/css2?family=Roboto:wght@300;400;500;700&display=swap">
<style>
  :root {
    --backdrop: #ece9e4;
    --card-white: #ffffff;
    --card-grey: #eeeeee;
    --green-dark: #2f9a3a;
    --green-mid: #6cb43c;
    --green-light: #a6d45a;
    --text-grey: #6a6a6a;
    --skyline-grey: #e2e2e2;
    --white: #ffffff;
  }
  * { box-sizing: border-box; margin: 0; padding: 0; }
  html, body { width: 1200px; height: 1023px; overflow: hidden; }
  body {
    background: var(--backdrop);
    font-family: "Roboto", Arial, sans-serif;
    position: relative;
  }
  .card {
    position: absolute;
    width: 560px;
    height: 320px;
    border-radius: 18px;
    overflow: hidden;
    box-shadow: 0 4px 0 #5aa332, 0 8px 0 #4e922b, 0 18px 30px rgba(0,0,0,.25);
  }
  /* front */
  .card-front {
    left: 60px; top: 150px;
    background: linear-gradient(160deg, var(--card-white) 30%, var(--card-grey) 100%);
  }
  .card-front .skyline {
    position: absolute; left: 250px; bottom: 0;
    width: 200px; height: 190px;
    background: linear-gradient(180deg, rgba(226,226,226,.2), var(--skyline-grey));
  }
  .card-front .swoosh { position: absolute; inset: 0; }
  .brand {
    position: absolute; left: 34px; top: 36px;
    display: flex; align-items: center; gap: 10px;
  }
  .brand-square { width: 16px; height: 16px; background: var(--green-dark); }
  .brand-name {
    font-size: 62px; font-weight: 700; color: var(--green-dark); line-height: 1;
  }
  .brand-tagline {
    position: absolute; left: 34px; top: 106px;
    font-size: 9px; letter-spacing: 1.6px; text-transform: uppercase;
    color: var(--text-grey);
  }
  .company {
    position: absolute; left: 214px; top: 52px;
    font-size: 26px; font-weight: 400; color: var(--green-mid);
    letter-spacing: .3px; white-space: nowrap;
  }
  .person { position: absolute; left: 34px; top: 134px; }
  .person-name { font-size: 24px; font-weight: 500; color: var(--green-dark); line-height: 30px; }
  .person-title { font-size: 15px; color: var(--text-grey); line-height: 20px; }
  .contacts { list-style: none; margin-top: 10px; }
  .contacts li {
    display: flex; align-items: center; gap: 8px;
    font-size: 13px; color: var(--text-grey); line-height: 19px;
  }
  .contacts svg { width: 12px; height: 12px; fill: var(--green-dark); flex: none; }
  /* back */
  .card-back {
    left: 580px; top: 560px;
    background: radial-gradient(circle at 70% 60%, var(--green-light), var(--green-mid) 70%);
  }
  .card-back .skyline {
    position: absolute; left: 30px; bottom: 0;
    width: 300px; height: 200px;
    background: linear-gradient(180deg, rgba(255,255,255,0), rgba(255,255,255,.12));
  }
  .back-brand {
    position: absolute; left: 0; right: 0; top: 88px;
    display: flex; flex-direction: column; align-items: center;
  }
  .back-brand .brand-row { display: flex; align-items: center; gap: 14px; }
  .back-brand .brand-square { width: 22px; height: 22px; background: var(--white); }
  .back-brand .brand-name { font-size: 110px; color: var(--white); }
  .back-brand .brand-tagline {
    position: static; color: var(--white); font-size: 13px; letter-spacing: 3px; margin-top: 10px;
  }
</style>
</head>
<body>

<section class="card card-front">
  <div class="skyline" role="img" aria-label="Faint city skyline silhouette"></div>
  <svg class="swoosh" viewBox="0 0 560 320" preserveAspectRatio="none" aria-hidden="true">
    <defs>
      <linearGradient id="band" x1="0" y1="0" x2="1" y2="1">
        <stop offset="0" stop-color="#6cb43c"/>
        <stop offset="1" stop-color="#a6d45a"/>
      </linearGradient>
    </defs>
    <path d="M560 0 L440 0 C420 120 380 230 330 320 L560 320 Z" fill="#ffffff"/>
    <path d="M560 0 L452 0 C432 120 394 230 346 320 L560 320 Z" fill="url(#band)"/>
    <path d="M444 0 C424 120 386 230 338 320" fill="none" stroke="#a6d45a" stroke-width="2"/>
  </svg>
  <div class="brand">
    <span class="brand-name">KVO</span>
    <span class="brand-square"></span>
  </div>
  <div class="brand-tagline">Keystone Value Overhauls</div>
  <h1 class="company">KVO Construction</h1>
  <div class="person">
    <h2 class="person-name">Danny Ferrante</h2>
    <p class="person-title">General Contractor</p>
    <ul class="contacts">
      <li><svg viewBox="0 0 12 12"><path d="M2 1h3l1 3-2 1a7 7 0 0 0 3 3l1-2 3 1v3a1 1 0 0 1-1 1A10 10 0 0 1 1 2a1 1 0 0 1 1-1z"/></svg>1-888-902-7315 Ext #1</li>
      <li><svg viewBox="0 0 12 12"><path d="M3 0h6a1 1 0 0 1 1 1v10a1 1 0 0 1-1 1H3a1 1 0 0 1-1-1V1a1 1 0 0 1 1-1zm0 2v7h6V2z"/></svg>215-730-4162</li>
      <li><svg viewBox="0 0 12 12"><path d="M3 0h6v4H3zM1 5h10v7H1zm2 2v1h2V7zm4 0v1h2V7zm-4 2v1h2V9zm4 0v1h2V9z"/></svg>1-888-902-7315</li>
      <li><svg viewBox="0 0 12 12"><path d="M0 2h12v8H0zm1 1v.4l5 3.3 5-3.3V3zm0 1.6V9h10V4.6L6 8z"/></svg>danny@kvoconstruction.com</li>
      <li><svg viewBox="0 0 12 12"><path d="M6 0a6 6 0 1 0 0 12A6 6 0 0 0 6 0zm0 1.2c.8.8 1.3 2.4 1.4 4.2H4.6C4.7 3.6 5.2 2 6 1.2zM1.3 5.4h2.1c0-1.4.4-2.8.9-3.8a4.8 4.8 0 0 0-3 3.8zm7.3 0h2.1a4.8 4.8 0 0 0-3-3.8c.5 1 .9 2.4.9 3.8zM1.3 6.6a4.8 4.8 0 0 0 3 3.8c-.5-1-.9-2.4-.9-3.8zm3.3 0c.1 1.8.6 3.4 1.4 4.2.8-.8 1.3-2.4 1.4-4.2zm4 0c0 1.4-.4 2.8-.9 3.8a4.8 4.8 0 0 0 3-3.8z"/></svg>www.kvoconstruction.com</li>
    </ul>
  </div>
</section>

<section class="card card-back">
  <div class="skyline" role="img" aria-label="Faint city skyline silhouette"></div>
  <div class="back-brand">
    <div class="brand-row">
      <span class="brand-name">KVO</span>
      <span class="brand-square"></span>
    </div>
    <div class="brand-tagline">Keystone Value Overhauls</div>
  </div>
</section>

</body>
</html>
```